Branded Postcard Design for Physician Gift

We’re looking for a clean, professional, and slightly playful postcard design to include inside branded Brevard tumblers being sent to physicians participating in a clinical pilot study.

The card should incorporate our KOR LUMEN TX logo and brand colors (magenta and navy — logo attached), and prominently feature the quote:

“Here’s to staying hydrated as we sprint to the finish line!”

We’d love a design that feels modern and clean — appropriate for a physician audience — with a subtle nod to hydration and the idea of approaching the study’s finish line (e.g., a small water droplet, a minimalist finish line/checkered flag, etc.).

Specs:

Size: Standard postcard (horizontal or vertical layout is fine)

Front: Main quote with design elements

Back: Optional space for a short thank-you message (can be left blank or designed with placeholder text)

Tone:
Professional but friendly, clean and visually appealing with minimal clutter.

I am totally open to your creative ideas - you do not need to follow this description exactly! I'd love to see your ideas. :)

```html
<!DOCTYPE html>
<html lang="en">
<head>
<meta charset="utf-8">
<title>KOR LUMEN TX Postcard</title>
<link rel="stylesheet" href="https://fonts.googleapis.com/css2?family=Poppins:wght@400;600&display=swap">
<style>
  :root {
    --backdrop: #c4c4c4;
    --card: #f0f0ed;
    --navy: #14203f;
    --magenta: #9c4280;
    --white: #ffffff;
  }
  * { margin: 0; padding: 0; box-sizing: border-box; }
  html, body { width: 837px; height: 1200px; overflow: hidden; }
  body {
    background: var(--backdrop);
    font-family: "Poppins", sans-serif;
    position: relative;
  }
  .postcard {
    position: absolute;
    left: 83px;
    width: 672px;
    height: 454px;
    background: var(--card);
    overflow: hidden;
  }
  .postcard--front { top: 87px; }
  .postcard--back { top: 613px; }
  .bands { position: absolute; left: 0; top: 0; width: 672px; height: 454px; }

  .headline {
    position: absolute;
    left: 36px;
    top: 62px;
    width: 410px;
    font-weight: 600;
    font-size: 46px;
    line-height: 56.5px;
    letter-spacing: -0.2px;
    white-space: nowrap;
    color: var(--navy);
  }
  .headline .accent { color: var(--magenta); }

  .flag-art {
    position: absolute;
    left: 465px;
    top: 83px;
    width: 154px;
    height: 140px;
    background: linear-gradient(135deg, var(--navy), #5b6480);
    border-radius: 4px;
  }

  .brand-name {
    position: absolute;
    right: 36px;
    font-weight: 600;
    font-size: 30px;
    letter-spacing: 1px;
    color: var(--magenta);
    white-space: nowrap;
  }
  .postcard--front .brand-name { top: 320px; }
  .postcard--back .brand-name { top: 325px; right: 44px; }

  .thanks-title {
    position: absolute;
    left: 45px;
    top: 62px;
    font-weight: 600;
    font-size: 47px;
    letter-spacing: 0.3px;
    color: var(--magenta);
  }
  .stamp-box {
    position: absolute;
    left: 567px;
    top: 42px;
    width: 65px;
    height: 65px;
    border: 1px solid var(--navy);
  }
  .address-line {
    position: absolute;
    left: 417px;
    width: 215px;
    border-top: 1px solid var(--navy);
  }
  .address-line--one { top: 160px; }
  .address-line--two { top: 200px; }

  .message {
    position: absolute;
    left: 45px;
    font-size: 20px;
    line-height: 24.5px;
    color: var(--navy);
  }
  .message--intro { top: 148px; width: 250px; }
  .message--body { top: 245px; width: 620px; }

  .signoff {
    position: absolute;
    left: 57px;
    top: 395px;
    font-size: 19px;
    color: var(--white);
  }
</style>
</head>
<body>

<section class="postcard postcard--front">
  <svg class="bands" viewBox="0 0 672 454" aria-hidden="true">
    <polygon points="0,375 369,375 385,454 0,454" fill="var(--navy)"/>
    <polygon points="377,421 672,421 672,454 384,454" fill="var(--magenta)"/>
    <path d="M176 337 C158 358 144 376 144 389 A32 32 0 0 0 208 389 C208 376 194 358 176 337 Z"
          fill="var(--magenta)" stroke="var(--card)" stroke-width="3"/>
  </svg>

  <h1 class="headline">Here’s to staying<br><span class="accent">hydrated</span> as we<br>sprint to the<br>finish line!</h1>

  <div class="flag-art" role="img" aria-label="Checkered finish-line flag illustration"></div>

  <div class="brand-name">KOR LUMEN TX</div>
</section>

<section class="postcard postcard--back">
  <svg class="bands" viewBox="0 0 672 454" aria-hidden="true">
    <polygon points="0,376 369,376 385,454 0,454" fill="var(--magenta)"/>
    <polygon points="377,422 672,422 672,454 384,454" fill="var(--navy)"/>
  </svg>

  <h2 class="thanks-title">THANK YOU</h2>
  <div class="stamp-box"></div>
  <div class="address-line address-line--one"></div>
  <div class="address-line address-line--two"></div>

  <p class="message message--intro">Thank you for being a<br>vital part of this clinical<br>pilot study.</p>
  <p class="message message--body">Your dedication and commitment help drive meaningful<br>progress — we’re truly grateful to have you on this journey.</p>

  <div class="brand-name">KOR LUMEN TX</div>

  <p class="signoff">- The KOR LUMEN TX Team</p>
</section>

</body>
</html>
```